Stonvale Depot needs a Self-Mailer Brochure Design

NOTE: DO NOT COPY OUR CURRENT BROCHURE DESIGN, WE DON'T LIKE IT AND LOOKING FOR SOMETHING NEW.

I am in charge of marketing at Stonvale Depot. I need create a new self-mailer brochure with our products.

Brief introduction:
• We are wholesaler specializing in home hardware and building supplies. We sell high-end products at better prices.
• Here's some of the items we sell: Bathtub Sales, Faucet Sales, Range Hood
Sales, Shower Sales, Sink Sales, Toilet Sales, Tile Sales, Kitchen supply
sales, Bathroom Supply Sales, Vanities, Lighting, Door Hardware, Mouldings etc.
• Areas Served: Greater Phoenix Area. We are trying to target local businesses in the Phoenix area. Our zip code is 85040.

We would like to create a new self-mailer brochure, that is going to
list our products. The current self-mailer brochure we have is not as organized as we need it to be. We need to make it well-organized and more efficient for our potential customers. I'm attaching our current self-mailer brochure as a reference, Please see the current self-mailer brochure to get an idea of what we need exactly, it will help you to come up with a better concept of putting it all together.

• On the first page, we'd like to include all the essential information about us, and our products- our logo and address, the discounts we provide, and the variety of products that we offer.
• On the other pages, we'd like to list our products with images and descriptions, just like in the current brochure.
• Please make it look appealing to the customer, start the listing with vanities/faucets/surfaces etc.
• You could include the "compare prices" section, just like in current brochure, but only on the first page, instead of every item (Our competitor is Drent, you can find it in the current brochure)
• We're open to suggestions, so please advise on the design (Simple clean lines, high-end, luxury theme would work best)
• Also, it is important to include all the necessary requirements for a self-mailer so we meet the required specification (you can find the requirements online)

Please find all the imagery and descriptions on our website- https://www.stonvaledepot-example.com/ - all the images in high res.
The format is 8/5X11", 2 pages, on both sides.

Please email me at quietlark.mira@mailtrove-example.com, or text me through the platform if you have any questions!
Current brochure and logo are attached,

Looking forward to hear back from you!

Mira

Target Market(s)

Local Businesses in Phoenix

Industry/Entity Type

Building Product

Font styles to use
Serif

Colors
abd036
000000
5c5c5c
ffffff

Requirements
Must have
• We would like to create a new self-mailer brochure, that is going to
• list our products. The current self-mailer brochure we have is not as organized as we need it to be. We need to make it well-organized and more efficient for our potential customers. I'm attaching our current self-mailer brochure as a reference, Please see the current self-mailer brochure to get an idea of what we need exactly, it will help you to come up with a better concept of putting it all together.
• • On the first page, we'd like to include all the essential information about us, and our products- our logo and address, the discounts we provide, and the variety of products that we offer.
• • On the other pages, we'd like to list our products with images and descriptions, just like in the current brochure.
• • Please make it look appealing to the customer, start the listing with vanities/faucets/surfaces etc. by category (check our website to get familiar with categories)
• • You could include the "compare prices" section, just like in current brochure, but only on the first page, instead of every item (Our competitor is Drent, you can find it in the current brochure)
• • We're open to suggestions, so please advise on the design (Simple clean lines, high-end, luxury theme would work best)
• • Also, it is important to include all the necessary requirements for a self-mailer so we meet the required specification (you can find the requirements online)

```html
<!DOCTYPE html>
<html lang="en">
<head>
<meta charset="utf-8">
<title>Stonvale Depot — Self-Mailer Brochure Spread</title>
<link rel="stylesheet" href="https://fonts.googleapis.com/css2?family=Playfair+Display:wght@400;600;700&family=Lora:ital,wght@0,400;0,600;1,400&display=swap">
<style>
  :root{
    --lime:#abd036;
    --black:#000000;
    --slate:#2b2b2b;
    --grey:#5c5c5c;
    --light:#d6d6d6;
    --white:#ffffff;
    --backdrop:#e6e6e8;
    --serif-display:"Playfair Display", Georgia, serif;
    --serif-text:"Lora", Georgia, serif;
  }
  *{box-sizing:border-box;margin:0;padding:0}
  html,body{width:1200px;height:1000px;overflow:hidden;background:var(--backdrop)}
  .canvas{position:relative;width:1200px;height:1000px}
  .spread{position:absolute;left:40px;top:137px;width:1120px;height:725px;display:flex;box-shadow:0 10px 30px rgba(0,0,0,.25)}
  .page{position:relative;width:560px;height:725px;overflow:hidden}
  .page--back{background:var(--black)}
  .page--front{background:var(--slate)}
  .accent{position:absolute;background:var(--lime)}
  .photo{position:absolute}

  /* category listings */
  .category{position:absolute;left:30px;width:500px}
  .category__head{display:flex;align-items:center;gap:14px;height:26px}
  .category__title{font:600 20px/1 var(--serif-display);color:var(--white);white-space:nowrap}
  .category__rule{flex:1;height:2px;background:var(--lime)}
  .product-grid{display:grid;grid-template-columns:repeat(5,1fr);gap:8px;margin-top:8px}
  .product{position:relative}
  .product__thumb{height:52px;background:linear-gradient(135deg,#f4f4f4,#b9b9b9)}
  .product__price{position:absolute;top:4px;right:4px;background:var(--lime);color:var(--black);font:600 10px/1 var(--serif-text);padding:3px 4px}
  .product__caption{color:var(--light);font:400 10px/1.2 var(--serif-text);margin-top:4px;white-space:nowrap}

  /* mailing panel */
  .mail-panel{position:absolute;left:20px;top:400px;width:520px;height:305px;background:var(--white);color:var(--black)}
  .return-address{position:absolute;left:22px;top:22px;font:400 11px/1.4 var(--serif-text)}
  .return-address__name{display:flex;align-items:center;gap:8px;font:700 16px/1 var(--serif-display);margin-bottom:6px}
  .return-address__mark{width:12px;height:12px;background:var(--lime)}
  .indicia{position:absolute;right:22px;top:22px;width:132px;border:1.5px solid var(--black);padding:8px 6px;text-align:center;font:600 9px/1.45 var(--serif-text);text-transform:uppercase;letter-spacing:.4px}
  .recipient{position:absolute;left:190px;top:150px;font:400 13px/1.5 var(--serif-text)}
  .recipient__line{text-transform:uppercase;letter-spacing:.5px}
  .mail-panel__note{position:absolute;left:22px;bottom:16px;font:italic 400 10px/1 var(--serif-text);color:var(--grey)}

  /* cover */
  .brand{position:absolute;left:40px;top:40px;display:flex;align-items:center;gap:14px}
  .brand__mark{width:22px;height:22px;background:var(--lime)}
  .brand__name{font:700 40px/1 var(--serif-display);color:var(--lime)}
  .tagline{position:absolute;left:40px;top:96px;font:italic 400 14px/1 var(--serif-text);color:var(--light)}
  .category-list{position:absolute;left:40px;top:135px;width:250px;list-style:none;display:grid;grid-template-columns:1fr 1fr;row-gap:6px;column-gap:12px;font:400 12px/1.2 var(--serif-text);color:var(--white);text-transform:uppercase;letter-spacing:.5px}
  .offer{position:absolute;left:300px;top:128px;width:210px;text-align:center;text-transform:uppercase}
  .offer__lead{font:600 20px/1.2 var(--serif-display);color:var(--white)}
  .offer__value{font:700 32px/1.15 var(--serif-display);color:var(--lime)}
  .offer__note{font:600 11px/1.3 var(--serif-text);color:var(--white);letter-spacing:.4px}

  .compare{position:absolute;left:30px;top:418px;width:470px}
  .compare__title{font:600 20px/1 var(--serif-display);color:var(--white);margin-bottom:10px}
  .compare__table{width:100%;border-collapse:collapse;font:400 12px/1 var(--serif-text);color:var(--white)}
  .compare__table th{font-weight:600;color:var(--lime);text-align:left;padding:6px 4px;border-bottom:1.5px solid var(--lime)}
  .compare__table td{padding:7px 4px;border-bottom:1px solid var(--grey)}
  .compare__table .num{text-align:right}
  .compare__table .ours{color:var(--lime);font-weight:600}

  .contact{position:absolute;left:30px;top:608px;width:470px}
  .contact__lead{font:600 16px/1.2 var(--serif-display);color:var(--lime)}
  .contact__phone{font:700 22px/1.3 var(--serif-display);color:var(--white);margin-top:4px}
  .contact__address{font:400 13px/1.3 var(--serif-text);color:var(--light);margin-top:4px}
</style>
</head>
<body>
<main class="canvas">
  <div class="spread">

    <!-- Back panel: listings and mailing panel -->
    <section class="page page--back">
      <div class="category" style="top:28px">
        <div class="category__head"><h2 class="category__title">Vanities</h2><span class="category__rule"></span></div>
        <div class="product-grid">
          <div class="product"><div class="product__thumb" role="img" aria-label="Vanity product photo"></div><span class="product__price">$749</span><p class="product__caption">60" Double Espresso</p></div>
          <div class="product"><div class="product__thumb" role="img" aria-label="Vanity product photo"></div><span class="product__price">$529</span><p class="product__caption">48" Grey Shaker</p></div>
          <div class="product"><div class="product__thumb" role="img" aria-label="Vanity product photo"></div><span class="product__price">$419</span><p class="product__caption">36" White Classic</p></div>
          <div class="product"><div class="product__thumb" role="img" aria-label="Vanity product photo"></div><span class="product__price">$389</span><p class="product__caption">30" Floating Oak</p></div>
          <div class="product"><div class="product__thumb" role="img" aria-label="Vanity product photo"></div><span class="product__price">$299</span><p class="product__caption">24" Compact Navy</p></div>
        </div>
      </div>

      <div class="category" style="top:146px">
        <div class="category__head"><h2 class="category__title">Faucets</h2><span class="category__rule"></span></div>
        <div class="product-grid">
          <div class="product"><div class="product__thumb" role="img" aria-label="Faucet product photo"></div><span class="product__price">$119</span><p class="product__caption">Tall Vessel Chrome</p></div>
          <div class="product"><div class="product__thumb" role="img" aria-label="Faucet product photo"></div><span class="product__price">$149</span><p class="product__caption">Pull-Down Kitchen</p></div>
          <div class="product"><div class="product__thumb" role="img" aria-label="Faucet product photo"></div><span class="product__price">$89</span><p class="product__caption">Widespread Nickel</p></div>
          <div class="product"><div class="product__thumb" role="img" aria-label="Faucet product photo"></div><span class="product__price">$199</span><p class="product__caption">Wall Tub Filler</p></div>
          <div class="product"><div class="product__thumb" role="img" aria-label="Faucet product photo"></div><span class="product__price">$69</span><p class="product__caption">Single Lever Black</p></div>
        </div>
      </div>

      <div class="category" style="top:264px">
        <div class="category__head"><h2 class="category__title">Surfaces</h2><span class="category__rule"></span></div>
        <div class="product-grid">
          <div class="product"><div class="product__thumb" role="img" aria-label="Tile product photo"></div><span class="product__price">$2.45</span><p class="product__caption">Porcelain Plank /sf</p></div>
          <div class="product"><div class="product__thumb" role="img" aria-label="Tile product photo"></div><span class="product__price">$7.95</span><p class="product__caption">Arabesque White</p></div>
          <div class="product"><div class="product__thumb" role="img" aria-label="Tile product photo"></div><span class="product__price">$6.95</span><p class="product__caption">Carrara Hex Mosaic</p></div>
          <div class="product"><div class="product__thumb" role="img" aria-label="Tile product photo"></div><span class="product__price">$3.95</span><p class="product__caption">Gloss Subway /sf</p></div>
          <div class="product"><div class="product__thumb" role="img" aria-label="Tile product photo"></div><span class="product__price">$5.45</span><p class="product__caption">Slate Grey /sf</p></div>
        </div>
      </div>

      <div class="mail-panel">
        <div class="return-address">
          <p class="return-address__name"><span class="return-address__mark"></span>Stonvale Depot</p>
          <p>1280 E. Harlan Ave.</p>
          <p>Phoenix, AZ 85040</p>
        </div>
        <div class="indicia">
          <p>Presorted Standard</p>
          <p>U.S. Postage Paid</p>
          <p>Phoenix, AZ</p>
          <p>Permit No. 0000</p>
        </div>
        <div class="recipient">
          <p class="recipient__line">Business Owner</p>
          <p class="recipient__line">Company Name</p>
          <p class="recipient__line">Street Address</p>
          <p class="recipient__line">Phoenix, AZ 850XX</p>
        </div>
        <p class="mail-panel__note">Or current business resident — Greater Phoenix Area</p>
      </div>
    </section>

    <!-- Front cover -->
    <section class="page page--front">
      <div class="brand"><span class="brand__mark"></span><p class="brand__name">Stonvale Depot</p></div>
      <p class="tagline">Wholesale home hardware &amp; building supplies</p>
      <ul class="category-list">
        <li>Bathroom</li><li>Kitchen</li><li>Vanities</li><li>Faucets</li><li>Moulding</li><li>Lighting</li><li>Door Hardware</li><li>Surfaces</li>
      </ul>

      <div class="offer">
        <p class="offer__lead">Save up to</p>
        <p class="offer__value">40–75% off</p>
        <p class="offer__note">Major retailer store price</p>
      </div>

      <div class="accent" style="left:522px;top:180px;width:38px;height:545px"></div>

      <div class="photo" role="img" aria-label="White vessel sink with tall chrome faucet" style="left:30px;top:240px;width:236px;height:156px;background:linear-gradient(135deg,#c4c4c4,#6e6e6e)"></div>
      <div class="photo" role="img" aria-label="Dark double vanity with framed mirror" style="left:274px;top:240px;width:226px;height:156px;background:linear-gradient(160deg,#e4e4e4,#7e7e7e)"></div>

      <div class="compare">
        <h2 class="compare__title">Compare Prices</h2>
        <table class="compare__table">
          <thead><tr><th>Item</th><th class="num">Drent</th><th class="num">Stonvale Depot</th><th class="num">You Save</th></tr></thead>
          <tbody>
            <tr><td>60" Double Vanity</td><td class="num">$1,499</td><td class="num ours">$749</td><td class="num">50%</td></tr>
            <tr><td>Vessel Sink Faucet</td><td class="num">$289</td><td class="num ours">$119</td><td class="num">59%</td></tr>
            <tr><td>Porcelain Tile, per sq ft</td><td class="num">$6.98</td><td class="num ours">$2.45</td><td class="num">65%</td></tr>
            <tr><td>4-Light Vanity Fixture</td><td class="num">$189</td><td class="num ours">$69</td><td class="num">63%</td></tr>
          </tbody>
        </table>
      </div>

      <div class="contact">
        <p class="contact__lead">We're ready to answer any questions!</p>
        <p class="contact__phone">(602) 555 - 0148</p>
        <p class="contact__address">1280 E. Harlan Ave., Phoenix, AZ 85040</p>
      </div>
    </section>

  </div>
</main>
</body>
</html>
```